"Orvana" - Ketamine Clinic - Save Minds and Heal Hearts!! -

I need a very nice modern happy brain themed warm website design for our cutting edge modern and caring ketamine IV infusion clinic that also offers talk therapy and telemedicine visits.
A great design using the color schemes in out logos (grey, white, purples and that need metallic fading colored effect in the logo).

```html
<!DOCTYPE html>
<html lang="en">
<head>
<meta charset="utf-8">
<title>Orvana — Ketamine Clinic</title>
<link href="https://fonts.googleapis.com/css2?family=Heebo:wght@400;500;600;700&family=Roboto:ital,wght@0,400;0,500;1,400&display=swap" rel="stylesheet">
<style>
:root{
  --purple:#6a00d9;
  --teal:#16d6c6;
  --mint:#d8f8f3;
  --mint-soft:#eefcf9;
  --grey-btn:#777e8f;
  --text:#1c1c2e;
  --muted:#8a8d99;
  --navy:#0e0c3b;
  --white:#fff;
}
*{margin:0;padding:0;box-sizing:border-box}
html,body{width:1200px;height:3848px;overflow:hidden}
body{position:relative;font-family:"Roboto",sans-serif;color:var(--text);background:var(--white)}
.abs{position:absolute}
h1,h2,h3,h4{font-family:"Heebo",sans-serif}
.logo{display:flex;align-items:center;gap:10px;font-family:"Heebo",sans-serif;font-weight:700;font-size:34px;color:var(--purple)}
.logo .dot{width:26px;height:26px;border-radius:50%;background:var(--purple)}
.contact-item{display:flex;gap:14px;align-items:flex-start;font-size:14px}
.contact-item b{display:block;font-weight:500;color:var(--text);font-size:14px;margin-bottom:3px}
.contact-item span{color:var(--muted)}
.btn{display:inline-flex;align-items:center;justify-content:center;border-radius:40px;background:var(--grey-btn);color:#fff;font-size:13px;font-weight:500}
.nav{display:flex;gap:42px;font-size:12px;font-weight:500;letter-spacing:1px;color:var(--text)}
.nav .active{color:var(--purple)}
.socials{display:flex;gap:14px}
.socials i{width:24px;height:24px;border-radius:50%;background:var(--purple);display:block}
.hero-card{left:106px;top:264px;width:566px;height:383px;background:linear-gradient(135deg,#f3f5f8,#e8f1f7);box-shadow:0 8px 30px rgba(0,0,0,.08);padding:58px 51px}
.hero-card h1{font-size:43px;line-height:51px;color:var(--purple);font-weight:600}
.hero-card .hl{background:linear-gradient(transparent 74%,var(--teal) 74%,var(--teal) 92%,transparent 92%)}
.hero-card p{margin-top:20px;font-size:13.5px;line-height:21px;color:var(--muted);width:400px}
.feature{top:849px;width:329px;height:261px;background:#fff;box-shadow:0 6px 30px rgba(0,0,0,.07);padding:38px 43px}
.feature.primary{background:var(--purple);height:287px;color:#fff}
.feature h3{margin-top:20px;font-size:21px;font-weight:500;color:var(--purple)}
.feature.primary h3{color:#fff}
.feature p{margin-top:10px;font-size:13px;line-height:20px;color:var(--muted)}
.feature.primary p{color:#fff}
.link{margin-top:20px;font-size:12px;font-weight:500;color:var(--purple);display:flex;align-items:center;gap:8px}
.feature.primary .link{color:#fff;margin-left:24px}
.about h2{font-size:29px;line-height:34px;color:var(--purple);font-weight:600}
.about p{font-size:13px;line-height:20px;color:var(--muted);margin-top:18px}
.checks{margin-top:64px;list-style:none}
.checks li{font-size:13px;color:var(--muted);display:flex;gap:14px;align-items:center;height:30px}
.services{top:1836px;left:0;width:1200px;height:909px;background:var(--purple);color:#fff}
.services h2{position:absolute;top:92px;width:100%;text-align:center;font-size:29px;font-weight:500}
.services .sub{position:absolute;top:146px;width:100%;text-align:center;font-size:13px;line-height:20px}
.svc{width:306px;height:249px;background:#fff;padding:32px 33px}
.svc h3{margin-top:18px;font-size:21px;font-weight:500;color:var(--purple)}
.svc p{margin-top:10px;font-size:13px;line-height:20px;color:var(--muted)}
.svc .link{margin-top:14px}
.testimonials{top:2745px;left:0;width:1200px;height:412px;background:var(--mint-soft)}
.testi-panel{left:120px;top:0;width:960px;height:412px;background:#fff;text-align:center}
.newsletter{top:3157px;left:0;width:1200px;height:234px;background:linear-gradient(90deg,#26284f,#1f2150 60%,#2a2c55)}
.footer{top:3391px;left:0;width:1200px;height:457px;background:var(--navy);color:#fff}
.footer h4{font-size:15px;font-weight:500}
.footer .list{list-style:none;font-size:13px}
.footer .muted{color:#8b8aa8;font-size:13px;line-height:20px}
</style>
</head>
<body>

<header class="abs" style="left:0;top:0;width:1200px;height:162px;background:#fff">
  <div class="abs logo" style="left:115px;top:34px"><i class="dot"></i>Orvana</div>
  <div class="abs contact-item" style="left:483px;top:33px">
    <svg width="26" height="26" viewBox="0 0 26 26" fill="none" stroke="#6a00d9" stroke-width="1.4"><rect x="2" y="6" width="22" height="16"/><path d="M2 6l11 9 11-9"/></svg>
    <div><b>Mail Us</b><span>hello@orvana.example</span></div>
  </div>
  <div class="abs" style="left:668px;top:30px;width:1px;height:45px;background:#e6e6ee"></div>
  <div class="abs contact-item" style="left:702px;top:33px">
    <svg width="26" height="26" viewBox="0 0 26 26" fill="none" stroke="#6a00d9" stroke-width="1.4"><path d="M6 3l4 5-2 3c1 3 4 6 7 7l3-2 5 4-2 4C12 24 2 14 2 5z"/></svg>
    <div><b>Call Us</b><span>(+021) 4410 592</span></div>
  </div>
  <div class="abs" style="left:873px;top:20px;width:1px;height:60px;background:#e6e6ee"></div>
  <div class="abs btn" style="left:925px;top:31px;width:157px;height:38px">Make Appointment</div>
  <div class="abs" style="left:115px;top:100px;width:970px;height:1px;background:#ececf2"></div>
  <nav class="abs nav" style="left:115px;top:125px"><span class="active">HOME</span><span>ABOUT US</span><span>SERVICES</span><span>CONTACT US</span></nav>
  <div class="abs socials" style="left:947px;top:120px"><i></i><i></i><i></i><i></i></div>
</header>

<section class="abs" style="left:0;top:162px;width:1200px;height:603px">
  <svg class="abs" width="1200" height="603" role="img" aria-label="Smiling clinician in a white coat with arms crossed in a bright infusion clinic">
    <defs><linearGradient id="heroPhoto" x1="0" y1="0" x2="1" y2="1"><stop offset="0" stop-color="#eef2f6"/><stop offset=".6" stop-color="#dfe6ee"/><stop offset="1" stop-color="#c9d2dc"/></linearGradient></defs>
    <rect width="1200" height="603" fill="url(#heroPhoto)"/>
  </svg>
  <svg class="abs" width="1200" height="603"><polygon points="0,0 617,0 270,603 0,603" fill="#6a00d9"/></svg>
</section>
<div class="abs hero-card">
  <h1>Save Minds And Heal <span class="hl">Hearts</span> With Ketamine Care</h1>
  <p>Caring IV ketamine infusions, talk therapy and telemedicine visits to help your brain find calm, clarity and hope.</p>
  <div class="btn" style="margin-top:22px;width:139px;height:45px">Contact Us</div>
</div>

<div class="abs feature" style="left:106px">
  <svg width="48" height="42" viewBox="0 0 48 42" fill="none" stroke="#6a00d9" stroke-width="1.6"><path d="M2 6l14-4 16 4 14-4v34l-14 4-16-4-14 4z"/><path d="M16 2v34M32 6v34"/><circle cx="24" cy="16" r="4"/></svg>
  <h3>Visit our Location</h3>
  <p>A calm, private infusion suite with soft light, warm blankets and a caring team by your side the whole time</p>
  <div class="link">View Location <span>→</span></div>
</div>
<div class="abs feature primary" style="left:435px">
  <svg width="50" height="40" viewBox="0 0 50 40" fill="none" stroke="#fff" stroke-width="1.6"><path d="M25 38L6 20A11 11 0 0125 7a11 11 0 0119 13z"/><path d="M2 20h12l4-7 6 14 5-9h19"/></svg>
  <h3>Emergency Call</h3>
  <p>In a hard moment? Call our care line any time and speak with a nurse who will help you find next steps</p>
  <div class="link">
    <svg width="12" height="12" viewBox="0 0 26 26" fill="#fff"><path d="M6 3l4 5-2 3c1 3 4 6 7 7l3-2 5 4-2 4C12 24 2 14 2 5z"/></svg>
    (+021) 4410 592</div>
</div>
<div class="abs feature" style="left:763px">
  <svg width="48" height="48" viewBox="0 0 48 48" fill="none" stroke="#6a00d9" stroke-width="1.6"><path d="M2 18l22-16 22 16v28H2z"/><path d="M2 18l22 16 22-16"/><rect x="11" y="10" width="26" height="17"/><path d="M16 16h16M16 21h12"/></svg>
  <h3>Send us a Message</h3>
  <p>Ask about ketamine infusions, insurance or a first consult and our intake team will reply within a day</p>
  <div class="link">Get Started <span>→</span></div>
</div>

<div class="abs" style="left:143px;top:1267px;width:413px;height:512px;background:var(--mint)"></div>
<div class="abs" role="img" aria-label="Nurse preparing a relaxed patient for an IV infusion" style="left:115px;top:1237px;width:405px;height:505px;background:linear-gradient(135deg,#d9dde3,#eef0f3 50%,#c8ccd4)"></div>
<section class="abs about" style="left:625px;top:1240px;width:450px">
  <h2>We offer modern Ketamine Infusion Therapy</h2>
  <p>We are proud to offer IV ketamine infusions for depression, anxiety, PTSD and chronic pain. Our doctors and nurses tailor each plan to your brain and your story, pairing infusions with talk therapy and follow-up care.</p>
  <p>Every session is monitored by licensed staff in a quiet, comfortable room. Between visits, telemedicine check-ins keep you supported, so healing keeps going long after you leave.</p>
  <ul class="checks">
    <li><svg width="14" height="12" viewBox="0 0 14 12" fill="none" stroke="#6a00d9" stroke-width="2"><path d="M1 6l4 4 8-9"/></svg>24 Hours Emergency Assistance Call Us</li>
    <li><svg width="14" height="12" viewBox="0 0 14 12" fill="none" stroke="#6a00d9" stroke-width="2"><path d="M1 6l4 4 8-9"/></svg>Medically supervised IV ketamine infusions</li>
    <li><svg width="14" height="12" viewBox="0 0 14 12" fill="none" stroke="#6a00d9" stroke-width="2"><path d="M1 6l4 4 8-9"/></svg>Talk therapy and telemedicine visits after every session</li>
  </ul>
  <div class="btn" style="margin-top:34px;width:138px;height:41px;font-size:12px">More About Us</div>
</section>

<section class="abs services">
  <h2>Our Brain Healthcare Services</h2>
  <div class="sub">Gentle, science-led care for a happier brain, from ketamine infusions<br>to talk therapy and virtual visits from home</div>
</section>
<div class="abs svc" style="left:115px;top:2111px">
  <svg width="48" height="48" viewBox="0 0 48 48" fill="none" stroke="#6a00d9" stroke-width="1.5"><circle cx="13" cy="9" r="5"/><circle cx="35" cy="9" r="5"/><circle cx="24" cy="24" r="3.5"/><path d="M5 36V20a8 8 0 0116 0v26M27 46V20a8 8 0 0116 0v16M19 46V32a5 5 0 0110 0"/></svg>
  <h3>Family Counseling</h3>
  <p>Sessions that help loved ones understand treatment and support healing</p>
  <div class="link">Read More <span>→</span></div>
</div>
<div class="abs svc" style="left:447px;top:2069px">
  <svg width="50" height="50" viewBox="0 0 50 50"><path d="M24 2C12 2 4 10 4 21c0 6 3 10 6 13v14h20v-7h7c3 0 5-2 5-5v-7l5-2-5-9C41 9 34 2 24 2z" fill="#6a00d9"/><circle cx="24" cy="21" r="6" fill="#fff"/><g stroke="#fff" stroke-width="2.5"><path d="M24 10v22M13 21h22M16 13l16 16M32 13L16 29"/></g><circle cx="24" cy="21" r="3" fill="#6a00d9"/></svg>
  <h3>Ketamine Infusion</h3>
  <p>Monitored IV ketamine sessions for depression, anxiety and PTSD</p>
  <div class="link">Read More <span>→</span></div>
</div>
<div class="abs svc" style="left:778px;top:2111px">
  <svg width="48" height="48" viewBox="0 0 48 48" fill="none" stroke="#6a00d9" stroke-width="1.5"><circle cx="17" cy="11" r="8"/><path d="M2 42c0-10 7-16 15-16 4 0 7 1 9 3"/><circle cx="34" cy="34" r="10"/><path d="M34 28v12M28 34h12"/></svg>
  <h3>Talk Therapy</h3>
  <p>One-to-one sessions that help you make sense of each infusion</p>
  <div class="link">Read More <span>→</span></div>
</div>
<div class="abs svc" style="left:115px;top:2395px">
  <svg width="48" height="48" viewBox="0 0 48 48" fill="none" stroke="#6a00d9" stroke-width="2"><path d="M6 18L24 6l18 12v24H6z"/><path d="M24 20v14M17 27h14"/></svg>
  <h3>Clinical Psychology</h3>
  <p>Careful assessment to find out if ketamine care is right for you</p>
  <div class="link">Read More <span>→</span></div>
</div>
<div class="abs svc" style="left:447px;top:2352px">
  <svg width="48" height="48" viewBox="0 0 48 48" fill="none" stroke="#6a00d9" stroke-width="2"><path d="M24 4C24 4 12 20 12 30a12 12 0 0024 0C36 20 24 4 24 4z"/><path d="M18 31a6 6 0 006 6"/></svg>
  <h3>Pain Management</h3>
  <p>Low-dose ketamine infusions to ease long-term nerve and body pain</p>
  <div class="link">Read More <span>→</span></div>
</div>
<div class="abs svc" style="left:778px;top:2395px">
  <svg width="52" height="48" viewBox="0 0 52 48" fill="none" stroke="#6a00d9" stroke-width="1.8"><rect x="6" y="10" width="40" height="26" rx="2"/><rect x="10" y="14" width="32" height="18"/><path d="M2 38h48l-3 4H5z"/><path d="M20 26l6-6M24 27l6-6"/></svg>
  <h3>Telemedicine Visits</h3>
  <p>Check in with your care team by video from the comfort of home</p>
  <div class="link">Read More <span>→</span></div>
</div>

<section class="abs testimonials">
  <div class="abs testi-panel">
    <div class="abs" style="left:0;top:84px;width:960px;font-size:15px;color:var(--muted)">Testimonials</div>
    <h2 class="abs" style="left:0;top:112px;width:960px;font-size:30px;font-weight:500;color:var(--purple)">What Patients Say About Us</h2>
    <svg class="abs" style="left:74px;top:118px" width="46" height="40" viewBox="0 0 46 40" fill="#6a00d9"><path d="M4 40V22C4 10 9 3 20 0l2 5c-6 2-9 6-9 12h8v23zM27 40V22c0-12 5-19 16-22l2 5c-6 2-9 6-9 12h8v23z"/></svg>
    <p class="abs" style="left:0;top:172px;width:960px;font-size:14.5px;line-height:21px;font-style:italic;color:var(--muted)">After years of trying everything, my ketamine infusions finally lifted the fog. The nurses were so warm and kind,<br>and the talk therapy sessions helped me keep that hope. I feel like myself again, and my family sees it too.</p>
    <div class="abs" role="img" aria-label="Patient portrait" style="left:455px;top:230px;width:50px;height:50px;border-radius:50%;border:3px solid var(--purple);background:linear-gradient(135deg,#e8c8b0,#b98d72)"></div>
    <div class="abs" style="left:0;top:300px;width:960px;font-family:'Heebo',sans-serif;font-size:15px;font-weight:500;color:var(--purple)">Mara Ellison</div>
  </div>
</section>

<section class="abs newsletter" role="img" aria-label="Dimmed photo of clinic staff behind the newsletter banner">
  <svg class="abs" style="left:115px;top:79px" width="32" height="34" viewBox="0 0 48 48" fill="none" stroke="#6a00d9" stroke-width="2"><path d="M2 18l22-16 22 16v28H2z"/><path d="M2 18l22 16 22-16"/><rect x="11" y="10" width="26" height="17"/></svg>
  <h3 class="abs" style="left:166px;top:76px;font-size:21px;font-weight:500;color:#fff">Subscribe To Our Newsletter</h3>
  <p class="abs" style="left:166px;top:110px;width:380px;font-size:13px;line-height:20px;color:#d8d8e8">Brain health tips, ketamine research news and clinic updates, sent once a month</p>
  <div class="abs" style="left:702px;top:98px;width:382px;height:48px;border-radius:30px;background:#fff;border:3px solid var(--purple)">
    <span class="abs" style="left:22px;top:13px;font-size:11px;color:#b5b7c2">Your Email Address</span>
    <span class="abs" style="right:1px;top:1px;width:128px;height:40px;border-radius:22px;background:var(--purple);color:#fff;font-size:12px;font-weight:500;display:flex;align-items:center;justify-content:center">Subscribe</span>
  </div>
</section>

<footer class="abs footer">
  <div class="abs logo" style="left:115px;top:82px;color:#fff"><i class="dot" style="background:#fff"></i>Orvana</div>
  <p class="abs muted" style="left:115px;top:226px;width:240px">Orvana is a modern ketamine clinic offering IV infusions, talk therapy and telemedicine visits to save minds and heal hearts.</p>
  <div class="abs socials" style="left:115px;top:322px;gap:17px"><i style="width:32px;height:32px"></i><i style="width:32px;height:32px"></i><i style="width:32px;height:32px"></i><i style="width:32px;height:32px"></i></div>

  <h4 class="abs" style="left:400px;top:70px">Contact Details</h4>
  <ul class="abs list" style="left:400px;top:136px;width:190px">
    <li style="display:flex;gap:16px;height:37px"><svg width="10" height="13" viewBox="0 0 10 13" fill="#6a00d9"><path d="M5 0a5 5 0 015 5c0 3-5 8-5 8S0 8 0 5a5 5 0 015-5z"/></svg>12 Harbor Lane, Westfield</li>
    <li style="display:flex;gap:16px;height:37px"><svg width="11" height="9" viewBox="0 0 11 9" fill="#6a00d9"><rect width="11" height="9"/></svg>care@orvana.example</li>
    <li style="display:flex;gap:16px;height:58px;line-height:20px"><svg width="11" height="11" viewBox="0 0 11 11" style="margin-top:5px"><circle cx="5.5" cy="5.5" r="5.5" fill="#6a00d9"/></svg>8 AM - 5 PM , Monday -<br>Saturday</li>
    <li style="display:flex;gap:16px"><svg width="11" height="11" viewBox="0 0 26 26" fill="#6a00d9"><path d="M6 3l4 5-2 3c1 3 4 6 7 7l3-2 5 4-2 4C12 24 2 14 2 5z"/></svg>(+021) 4410 592</li>
  </ul>

  <h4 class="abs" style="left:659px;top:70px">Other Pages</h4>
  <ul class="abs list" style="left:659px;top:136px">
    <li style="height:33px"><span style="color:#6a00d9;margin-right:14px">›</span>Home</li>
    <li style="height:33px"><span style="color:#6a00d9;margin-right:14px">›</span>About Us</li>
    <li style="height:33px"><span style="color:#6a00d9;margin-right:14px">›</span>Services</li>
    <li style="height:33px"><span style="color:#6a00d9;margin-right:14px">›</span>Our Doctor</li>
    <li><span style="color:#6a00d9;margin-right:14px">›</span>Contact</li>
  </ul>

  <h4 class="abs" style="left:846px;top:70px">Make Appointment</h4>
  <p class="abs muted" style="left:846px;top:136px;width:240px">Book a free consult to see if ketamine infusion care suits you</p>

  <div class="abs" style="left:115px;top:400px;width:970px;height:1px;background:#23214d"></div>
  <div class="abs muted" style="left:115px;top:418px;font-size:11px">Orvana. All Rights Reserved.</div>
  <div class="abs muted" style="right:115px;top:418px;font-size:11px">Copyright © 2021 All rights reserved.</div>
</footer>

</body>
</html>
```